job vacancy cover page

I need to design a one pager for a job I'd like to apply for. The one I have done looks shit and amateur!! Wanting it to look amazing and professional (Not too professional though as they are pretty young and fun).

```html
<!DOCTYPE html>
<html lang="en">
<head>
<meta charset="utf-8">
<title>Upward Lane – Cover Page</title>
<link href="https://fonts.googleapis.com/css2?family=Teko:wght@500;600&family=Montserrat:wght@300;400;600&display=swap" rel="stylesheet">
<style>
:root{
  --navy:#2b2c7f;
  --navy-soft:#31348f;
  --ink-navy:#2b2f86;
  --blue:#0063ff;
  --blue-soft:#0a55dc;
  --blue-ink:#0a5bd8;
  --text:#2a2a3a;
  --white:#ffffff;
  --rule:#dcdce4;
}
*{box-sizing:border-box;margin:0;padding:0}
html,body{width:1200px;height:2583px;overflow:hidden;background:var(--white)}
body{position:relative;font-family:"Montserrat",sans-serif;color:var(--text)}
.abs{position:absolute}
.display{font-family:"Teko",sans-serif;font-weight:600;line-height:1;white-space:nowrap}

/* hero */
.hero{left:0;top:0;width:1200px;height:615px;background:var(--navy);overflow:hidden}
.hero-disc{border-radius:50%;background:var(--navy-soft)}
.brand{font-family:"Teko",sans-serif;font-weight:600;color:var(--white);font-size:42px;line-height:1;text-align:center;width:100%}
.welcome{left:140px;top:247px;color:var(--white);font-size:25px}
.hero-title{left:140px;top:278px;color:var(--white);font-size:68px}
.btn{left:144px;top:374px;width:120px;height:39px;background:var(--white);color:var(--ink-navy);font-size:15px;display:flex;align-items:center;justify-content:center}
.hero-photo{left:632px;top:120px;width:453px;height:453px;border-radius:8px;background:linear-gradient(135deg,#ecebe8 0%,#c9c2b8 45%,#3d3f58 100%)}

/* feature cards */
.card{border-radius:14px}
.card-why-me{left:144px;top:695px;width:431px;height:384px;background:var(--navy)}
.card-why-us{left:614px;top:1563px;width:431px;height:383px;background:var(--blue)}
.card-title{color:var(--white);font-size:66px}

/* blocks */
.photo{border-radius:10px}
.h-navy{color:var(--ink-navy);font-size:41px}
.h-blue{color:var(--blue-ink);font-size:41px}
.list{list-style:none}
.list li{display:flex;align-items:flex-start;gap:12px}
.list svg{flex:none;margin-top:3px}
.lead{font-weight:600;font-size:16px;color:#1d1d2b;white-space:nowrap}
.rule{left:140px;top:1498px;width:910px;height:1px;background:var(--rule)}

/* footer */
.footer{left:0;top:2367px;width:1200px;height:216px;background:var(--navy);color:var(--white)}
.footer p{font-size:14.5px;line-height:24px;text-align:center;font-weight:300}
.footer-rule{left:144px;top:143px;width:909px;height:1px;background:var(--white)}
.copy{font-size:11px;font-weight:600;text-align:center;width:100%}
</style>
</head>
<body>

<header class="abs hero">
  <div class="abs hero-disc" style="left:35px;top:157px;width:280px;height:280px"></div>
  <div class="abs hero-disc" style="left:850px;top:285px;width:320px;height:320px"></div>
  <svg class="abs" style="left:0;top:0" width="1200" height="615" aria-hidden="true">
    <path d="M1085 345 A100 100 0 0 1 1085 545" fill="none" stroke="#c9cbf0" stroke-width="1.2"/>
    <g stroke="#fff" stroke-width="3" stroke-linecap="round">
      <line x1="145" y1="48" x2="175" y2="48"/>
      <line x1="150" y1="58" x2="175" y2="58"/>
      <line x1="145" y1="68" x2="175" y2="68"/>
    </g>
    <circle cx="1039" cy="56" r="10" fill="none" stroke="#fff" stroke-width="2.5"/>
    <line x1="1046" y1="63" x2="1053" y2="70" stroke="#fff" stroke-width="2.5" stroke-linecap="round"/>
  </svg>
  <div class="abs brand" style="left:0;top:42px">Upward Lane</div>
  <div class="abs display welcome">Welcome To</div>
  <h1 class="abs display hero-title">Upward Lane</h1>
  <div class="abs btn">Get Started</div>
  <div class="abs hero-photo" role="img" aria-label="Photo of two business people shaking hands across a desk"></div>
</header>

<section class="abs card card-why-me">
  <svg class="abs" style="left:-34px;top:52px;overflow:visible" width="400" height="300" aria-hidden="true">
    <line x1="230" y1="180" x2="384" y2="268" stroke="var(--navy-soft)" stroke-width="28" stroke-linecap="round"/>
    <circle cx="142" cy="140" r="140" fill="var(--navy-soft)"/>
  </svg>
  <h2 class="abs display card-title" style="left:64px;top:106px">Why Me?</h2>
</section>

<div class="abs photo" style="left:607px;top:695px;width:430px;height:131px;background:linear-gradient(180deg,#e9e2d6 0%,#d8b46b 55%,#f6d400 100%)" role="img" aria-label="Wooden letter blocks spelling profession being changed to passion"></div>
<h2 class="abs display h-navy" style="left:607px;top:853px">Passion</h2>
<ul class="abs list" style="left:608px;top:920px;width:440px;font-size:16.5px;line-height:27px;font-weight:300">
  <li style="margin-bottom:27px"><svg width="20" height="24"><circle cx="10" cy="10" r="7" fill="none" stroke="#333" stroke-width="1.5"/><circle cx="14" cy="18" r="5" fill="#3aa64a"/></svg>The development of others and / or their teams.</li>
  <li style="margin-bottom:27px"><svg width="20" height="24"><circle cx="10" cy="10" r="7" fill="none" stroke="#333" stroke-width="1.5"/><circle cx="14" cy="18" r="5" fill="#3aa64a"/></svg>Helping people learn and be successful in life and in their careers.</li>
  <li><svg width="20" height="24"><circle cx="10" cy="10" r="7" fill="none" stroke="#333" stroke-width="1.5"/><circle cx="14" cy="18" r="5" fill="#3aa64a"/></svg>Exceptional client experiences</li>
</ul>

<h2 class="abs display h-navy" style="left:145px;top:1150px">If I Was A Superhero</h2>
<p class="abs lead" style="left:146px;top:1219px">My Four Superpowers Would Be:</p>
<ul class="abs list" style="left:146px;top:1263px;font-size:16.5px;line-height:24px;font-weight:300">
  <li style="margin-bottom:14px"><svg width="18" height="18"><path d="M3 15 L14 4 M9 4 L14 4 L14 9" stroke="#d8232a" stroke-width="2.5" fill="none"/><circle cx="5" cy="13" r="2.5" fill="#2b5bd8"/></svg>Proactiveness</li>
  <li style="margin-bottom:14px"><svg width="18" height="18"><path d="M3 15 L14 4 M9 4 L14 4 L14 9" stroke="#d8232a" stroke-width="2.5" fill="none"/><circle cx="5" cy="13" r="2.5" fill="#2b5bd8"/></svg>Creativity</li>
  <li style="margin-bottom:14px"><svg width="18" height="18"><path d="M3 15 L14 4 M9 4 L14 4 L14 9" stroke="#d8232a" stroke-width="2.5" fill="none"/><circle cx="5" cy="13" r="2.5" fill="#2b5bd8"/></svg>Pride in my work</li>
  <li><svg width="18" height="18"><path d="M3 15 L14 4 M9 4 L14 4 L14 9" stroke="#d8232a" stroke-width="2.5" fill="none"/><circle cx="5" cy="13" r="2.5" fill="#2b5bd8"/></svg>Organisational skills</li>
</ul>
<div class="abs photo" style="left:473px;top:1135px;width:110px;height:278px;background:linear-gradient(180deg,#bdeff4 0%,#5fbfcf 55%,#2b9bb0 100%)" role="img" aria-label="Illustration of a businesswoman standing before a city skyline"></div>

<h2 class="abs display h-navy" style="left:600px;top:1155px">Some Of My Success</h2>
<ul class="abs list" style="left:600px;top:1210px;width:345px;font-size:14.5px;line-height:27px;font-weight:300">
  <li style="margin-bottom:27px"><svg width="20" height="18"><path d="M4 3 H16 L14 10 H6 Z" fill="#f2b71c"/><rect x="7" y="12" width="6" height="3" fill="#7fb34a"/></svg>Increased client workshops by 85% across accounts.</li>
  <li style="margin-bottom:27px"><svg width="20" height="18"><path d="M4 3 H16 L14 10 H6 Z" fill="#f2b71c"/><rect x="7" y="12" width="6" height="3" fill="#7fb34a"/></svg>Delivered double digit revenue increase.</li>
  <li><svg width="20" height="18"><path d="M4 3 H16 L14 10 H6 Z" fill="#f2b71c"/><rect x="7" y="12" width="6" height="3" fill="#7fb34a"/></svg>Re-designed workshops for virtual delivery, maintaining key relationships.</li>
</ul>
<div class="abs photo" style="left:947px;top:1145px;width:105px;height:276px;background:linear-gradient(180deg,#d8c7c0 0%,#b08468 50%,#3a2620 100%)" role="img" aria-label="Photo of climbers on a summit raising a trophy at sunset"></div>

<div class="abs rule"></div>

<div class="abs photo" style="left:145px;top:1564px;width:430px;height:130px;background:linear-gradient(180deg,#f3dcd9 0%,#ecd0ca 60%,#e5c37a 100%)" role="img" aria-label="Hands holding up gold balloon letters spelling values"></div>
<h2 class="abs display h-blue" style="left:145px;top:1719px">Values That Stood Out</h2>
<ul class="abs list" style="left:146px;top:1787px;font-size:16.5px;line-height:29px;font-weight:300">
  <li><svg width="18" height="22"><circle cx="9" cy="9" r="7" fill="#f5c518" stroke="#333" stroke-width="1.4"/><rect x="6" y="16" width="6" height="4" fill="#333"/></svg>Change for the better</li>
  <li><svg width="18" height="22"><circle cx="9" cy="9" r="7" fill="#f5c518" stroke="#333" stroke-width="1.4"/><rect x="6" y="16" width="6" height="4" fill="#333"/></svg>Excellence – not mediocre</li>
  <li><svg width="18" height="22"><circle cx="9" cy="9" r="7" fill="#f5c518" stroke="#333" stroke-width="1.4"/><rect x="6" y="16" width="6" height="4" fill="#333"/></svg>Put your heart into it and give a shit</li>
  <li><svg width="18" height="22"><circle cx="9" cy="9" r="7" fill="#f5c518" stroke="#333" stroke-width="1.4"/><rect x="6" y="16" width="6" height="4" fill="#333"/></svg>Going the extra mile</li>
  <li><svg width="18" height="22"><circle cx="9" cy="9" r="7" fill="#f5c518" stroke="#333" stroke-width="1.4"/><rect x="6" y="16" width="6" height="4" fill="#333"/></svg>Take risks</li>
</ul>

<section class="abs card card-why-us">
  <svg class="abs" style="left:-34px;top:52px;overflow:visible" width="400" height="300" aria-hidden="true">
    <line x1="230" y1="180" x2="384" y2="270" stroke="var(--blue-soft)" stroke-width="28" stroke-linecap="round"/>
    <circle cx="142" cy="140" r="140" fill="var(--blue-soft)"/>
  </svg>
  <h2 class="abs display card-title" style="left:64px;top:100px;line-height:1.05">Why Upward<br>Lane?</h2>
</section>

<h2 class="abs display h-blue" style="left:145px;top:2018px">What You Offer</h2>
<ul class="abs list" style="left:146px;top:2082px;font-size:16.5px;line-height:24px;font-weight:300">
  <li style="margin-bottom:14px"><svg width="18" height="18"><path d="M3 15 L14 4 M9 4 L14 4 L14 9" stroke="#d8232a" stroke-width="2.5" fill="none"/><circle cx="5" cy="13" r="2.5" fill="#2b5bd8"/></svg>Learning &amp; Developing</li>
  <li style="margin-bottom:14px"><svg width="18" height="18"><path d="M3 15 L14 4 M9 4 L14 4 L14 9" stroke="#d8232a" stroke-width="2.5" fill="none"/><circle cx="5" cy="13" r="2.5" fill="#2b5bd8"/></svg>Team</li>
  <li style="margin-bottom:14px"><svg width="18" height="18"><path d="M3 15 L14 4 M9 4 L14 4 L14 9" stroke="#d8232a" stroke-width="2.5" fill="none"/><circle cx="5" cy="13" r="2.5" fill="#2b5bd8"/></svg>Flexibility</li>
  <li><svg width="18" height="18"><path d="M3 15 L14 4 M9 4 L14 4 L14 9" stroke="#d8232a" stroke-width="2.5" fill="none"/><circle cx="5" cy="13" r="2.5" fill="#2b5bd8"/></svg>Fun</li>
</ul>
<div class="abs photo" style="left:458px;top:2004px;width:109px;height:276px;background:linear-gradient(180deg,#3a3f2e 0%,#8b8a5c 45%,#c9c6c2 100%)" role="img" aria-label="Photo of a smiling woman wearing a headset"></div>

<h2 class="abs display h-blue" style="left:600px;top:2014px">Interesting Projects</h2>
<ul class="abs list" style="left:600px;top:2070px;width:340px;font-size:14.5px;line-height:27px;font-weight:300">
  <li style="margin-bottom:27px"><svg width="20" height="18"><path d="M4 3 H16 L14 10 H6 Z" fill="#f2b71c"/><rect x="7" y="12" width="6" height="3" fill="#7fb34a"/></svg>Norvale - Leadership development and team effectiveness</li>
  <li style="margin-bottom:27px"><svg width="20" height="18"><path d="M4 3 H16 L14 10 H6 Z" fill="#f2b71c"/><rect x="7" y="12" width="6" height="3" fill="#7fb34a"/></svg>Hartwell – Change management for true transformation</li>
  <li><svg width="20" height="18"><path d="M4 3 H16 L14 10 H6 Z" fill="#f2b71c"/><rect x="7" y="12" width="6" height="3" fill="#7fb34a"/></svg>Lindell – Customer centricity at Australia's most iconic department store</li>
</ul>
<div class="abs photo" style="left:947px;top:2002px;width:105px;height:276px;background:linear-gradient(160deg,#e9e6e2 0%,#d6d0c8 55%,#a79c90 100%)" role="img" aria-label="Top-down photo of a team working at a desk with laptops"></div>

<footer class="abs footer">
  <div class="abs brand" style="left:0;top:24px">Upward Lane</div>
  <p class="abs" style="left:0;top:84px;width:1200px">Lorem ipsum dolor sit amet, consectetur adipiscing elit, sed do eiusmod tempor incididunt ut labore et dolore magna aliqua.<br>Quis ipsum suspendisse ultrices gravida. Risus commodo viverra maecenas accumsan lacus vel facilisis.</p>
  <div class="abs footer-rule"></div>
  <div class="abs copy" style="left:0;top:168px">© copyrights 2022 Upward Lane | &nbsp;All Rights Reserved</div>
</footer>

</body>
</html>
```